Flyer Design & Business Cards

I have tried to make up some flyer and have attached them as info with what we would like included. I would like them made to look more professional and I would like business cards along the same line.

Industry/Entity Type

Business

```html
<!DOCTYPE html>
<html lang="en">
<head>
<meta charset="utf-8">
<title>Harbourfold Inn – Business Cards</title>
<link rel="stylesheet" href="https://fonts.googleapis.com/css2?family=Lato:wght@400;700&family=Uncial+Antiqua&display=swap">
<style>
  :root {
    --page-bg: #e4e4e4;
    --card-blue: #135c85;
    --gold: #f4ad35;
    --accent-red: #c0272d;
    --frame-blue: #1d6a96;
    --illustration-fill: #7fc6e8;
    --exterior-top: #8a9aa8;
    --exterior-bottom: #6d6a62;
    --fireplace-fill: #9a6a3c;
    --bar-fill: #6a4a34;
  }
  * { margin: 0; padding: 0; box-sizing: border-box; }
  html, body { width: 1200px; height: 869px; overflow: hidden; }
  body {
    background: var(--page-bg);
    font-family: "Lato", sans-serif;
    position: relative;
  }
  .card {
    position: absolute;
    width: 640px;
    height: 355px;
    background: var(--card-blue);
    box-shadow: 0 2px 6px rgba(0,0,0,0.25);
    overflow: hidden;
  }
  .card--front { left: 97px; top: 63px; }
  .card--back { left: 459px; top: 450px; }

  /* Front: photo collage */
  .photo { position: absolute; }
  .photo--exterior {
    left: 0; top: 0; width: 241px; height: 219px;
    background: linear-gradient(180deg, var(--exterior-top) 0%, var(--exterior-bottom) 100%);
  }
  .photo--fireplace {
    left: 0; top: 221px; width: 123px; height: 134px;
    background: var(--fireplace-fill);
  }
  .photo--bottles {
    left: 125px; top: 221px; width: 116px; height: 134px;
    background: var(--bar-fill);
  }
  .collage-divider { position: absolute; background: var(--frame-blue); }
  .collage-divider--h { left: 0; top: 219px; width: 241px; height: 2px; }
  .collage-divider--v { left: 123px; top: 221px; width: 2px; height: 134px; }
  .accent-stripe {
    position: absolute; left: 241px; top: 0; width: 5px; height: 355px;
    background: var(--accent-red);
  }

  /* Front: name and address */
  .title-frame {
    position: absolute; left: 271px; top: 77px; width: 346px; height: 80px;
    border-left: 2px solid var(--gold);
    border-right: 2px solid var(--gold);
  }
  .inn-name {
    position: absolute; left: 246px; width: 394px; top: 80px;
    text-align: center; color: var(--gold);
    font-family: "Uncial Antiqua", serif;
    font-weight: 400; font-size: 40px; line-height: 50px;
  }
  .address {
    position: absolute; left: 246px; width: 394px; top: 210px;
    text-align: center; color: var(--gold);
    font-size: 24px; line-height: 27.5px; font-style: normal;
  }

  /* Back */
  .rule {
    position: absolute; left: 64px; width: 512px; height: 2px;
    background: var(--gold);
  }
  .rule--top { top: 30px; }
  .rule--bottom { top: 326px; }
  .ship-illustration {
    position: absolute; left: 50px; top: 91px; width: 218px; height: 160px;
    background: var(--illustration-fill);
  }
  .contact {
    position: absolute; left: 300px; width: 300px; top: 76px;
    text-align: center; color: var(--gold);
  }
  .contact__names {
    font-weight: 700; font-size: 36px; line-height: 44px;
  }
  .contact__names .joiner { font-size: 28px; }
  .contact__phone {
    margin-top: 14px; font-size: 26px; line-height: 30px;
  }
  .contact__web {
    font-size: 25px; line-height: 30px;
  }
</style>
</head>
<body>
  <section class="card card--front" aria-label="Business card front">
    <div class="photo photo--exterior" role="img" aria-label="Photograph of the stone-built inn"></div>
    <div class="collage-divider collage-divider--h"></div>
    <div class="photo photo--fireplace" role="img" aria-label="Photograph of a wood-burning stove"></div>
    <div class="collage-divider collage-divider--v"></div>
    <div class="photo photo--bottles" role="img" aria-label="Photograph of bottles on the bar shelf"></div>
    <div class="accent-stripe"></div>

    <div class="title-frame"></div>
    <h1 class="inn-name">Harbourfold<br>Inn</h1>
    <address class="address">
      Harbourfold Inn<br>
      Baile Mhor<br>
      Isle of Tarran<br>
      HS9 2QT
    </address>
  </section>

  <section class="card card--back" aria-label="Business card back">
    <div class="rule rule--top"></div>
    <div class="ship-illustration" role="img" aria-label="Illustration of a sailing ship"></div>
    <div class="contact">
      <p class="contact__names">Morag <span class="joiner">and</span> Ewan<br>Lindsay</p>
      <p class="contact__phone">01870 555142</p>
      <p class="contact__web">www.harbourfoldinn.com</p>
    </div>
    <div class="rule rule--bottom"></div>
  </section>
</body>
</html>
```